Looking to Rebrand landscaping business

Hello, Im looking for a flyer to be created. Basically something clean that gets the point across. These flyers will be distributed door to door throughout the community. I want a design that is simple to read and allows the eye to flow along through it, nothing crammed.
Here is a design i love. http://www.artbidhub.net/design/4839201
Services we offer:
Lawn Maintenance
Landscaping Services
Aeration
Thatch Removal
Fertilizer & Weed Control Applications (Programs Available)
Spring & Fall Clean ups
New Lawn Installations
Pruning
Mulch and rock Installation
Hedge Trimming
Winter Snow Removal Services
& more
Would like to have a special of:
Let us earn your Business
call now and get your first cut free of charge.
*conditions apply
Other points which COULD be included
Free Estimates
Fully Insured
Email: ADMIN@BRIARTOPLANDSCAPING.CA
PHONE: 506-384-9057
Serving Saint John & Surrounding Areas
I will be rebranding the complete business and interested in having more work done in the future.
Landscaping

```html
<!DOCTYPE html>
<html lang="en">
<head>
<meta charset="utf-8">
<title>Briartop Landscaping Flyer</title>
<link href="https://fonts.googleapis.com/css2?family=Arimo:wght@400;700&family=Exo+2:wght@700&display=swap" rel="stylesheet">
<style>
  :root {
    --green: #2e9a2e;
    --green-dark: #1f7d22;
    --green-bright: #4cc23a;
    --service-red: #9a1414;
    --mauve: #9c6f6f;
    --olive: #7f7a1c;
    --white: #ffffff;
    --sky: #dff3f8;
    --photo-top: #5f8a3e;
    --photo-bottom: #3f7a2a;
  }
  * { margin: 0; padding: 0; box-sizing: border-box; }
  html, body { width: 900px; height: 1200px; overflow: hidden; background: #f2f2f2; }
  .flyer {
    position: relative; width: 900px; height: 1200px; overflow: hidden;
    font-family: "Arimo", Arial, sans-serif;
    background: linear-gradient(180deg, var(--white) 60%, var(--sky) 100%);
  }
  .garden-photo {
    position: absolute; left: 0; top: 0; width: 900px; height: 500px;
    background:
      radial-gradient(ellipse at 70% 35%, #8fb86a 0%, transparent 55%),
      radial-gradient(ellipse at 20% 70%, #c9c43a 0%, transparent 35%),
      linear-gradient(180deg, #3d5f2a 0%, var(--photo-top) 40%, var(--photo-bottom) 100%);
  }
  .brand {
    position: absolute; left: 0; top: 14px; width: 400px; height: 80px;
    background: linear-gradient(90deg, rgba(255,255,255,.95) 55%, rgba(255,255,255,0));
    display: flex; align-items: center; padding-left: 30px; gap: 10px;
  }
  .brand-name { font-size: 46px; font-weight: 400; color: var(--green-dark); letter-spacing: 1px; }
  .brand-dot { width: 16px; height: 16px; border-radius: 50%; background: var(--green-dark); }
  .headline-top {
    position: absolute; left: 0; top: 500px; width: 900px; height: 96px;
    background: linear-gradient(180deg, var(--green-dark), var(--green));
    color: var(--white); font-weight: 700; font-size: 84px; text-align: center; line-height: 96px;
    letter-spacing: 1px;
  }
  .headline-bottom {
    position: absolute; left: 0; top: 596px; width: 900px; height: 80px;
    background: linear-gradient(180deg, var(--green), var(--green-dark));
    border-top: 2px solid #7dcf5a;
    color: var(--white); font-weight: 700; font-size: 64px; text-align: center; line-height: 76px;
  }
  .services { position: absolute; list-style: none; font-family: "Exo 2", sans-serif; font-weight: 700; color: var(--service-red); font-size: 19px; }
  .services li { display: flex; align-items: flex-start; gap: 12px; margin-bottom: 13px; line-height: 1.05; }
  .services svg { flex: none; margin-top: 1px; }
  .services-left { left: 48px; top: 700px; }
  .services-right { left: 500px; top: 738px; }
  .special-offer {
    position: absolute; left: 0; top: 932px; width: 900px; text-align: center;
    color: var(--green-dark); font-weight: 700;
  }
  .offer-title { font-size: 26px; line-height: 30px; }
  .offer-terms { font-size: 17px; line-height: 22px; color: var(--service-red); }
  .divider { position: absolute; left: 0; top: 992px; width: 900px; height: 4px; background: var(--green-bright); }
  .free-estimates, .fully-insured { position: absolute; top: 1002px; font-weight: 700; font-size: 36px; line-height: 66px; }
  .free-estimates { left: 40px; color: var(--mauve); }
  .fully-insured { right: 40px; color: var(--olive); }
  .free-estimates .big, .fully-insured .big { font-size: 62px; }
  .contact-bar {
    position: absolute; left: 0; top: 1076px; width: 900px; height: 64px;
    background: var(--green); color: var(--white); font-weight: 700;
    display: flex; align-items: center;
  }
  .phone { width: 470px; padding-left: 40px; font-size: 32px; border-right: 2px solid var(--white); height: 44px; line-height: 44px; }
  .email { padding-left: 30px; font-size: 17px; line-height: 1.3; }
  .service-area { position: absolute; left: 0; top: 1152px; width: 900px; text-align: center; color: var(--olive); font-weight: 700; font-size: 26px; line-height: 32px; }
</style>
</head>
<body>
<main class="flyer">
  <div class="garden-photo" role="img" aria-label="Landscaped garden with yellow lilies, curving stone path, rock beds and green lawn"></div>
  <div class="brand"><span class="brand-name">briartop</span><span class="brand-dot"></span></div>

  <h1 class="headline-top">A SERVICE FOR</h1>
  <h2 class="headline-bottom">EVERY SEASON</h2>

  <ul class="services services-left">
    <li><svg width="18" height="18" viewBox="0 0 18 18"><circle cx="9" cy="9" r="8" fill="#4cc23a"/><circle cx="9" cy="9" r="4" fill="#fff"/></svg>Lawn Maintenance</li>
    <li><svg width="18" height="18" viewBox="0 0 18 18"><circle cx="9" cy="9" r="8" fill="#4cc23a"/><circle cx="9" cy="9" r="4" fill="#fff"/></svg>Landscaping Services</li>
    <li><svg width="18" height="18" viewBox="0 0 18 18"><circle cx="9" cy="9" r="8" fill="#4cc23a"/><circle cx="9" cy="9" r="4" fill="#fff"/></svg>Aeration</li>
    <li><svg width="18" height="18" viewBox="0 0 18 18"><circle cx="9" cy="9" r="8" fill="#4cc23a"/><circle cx="9" cy="9" r="4" fill="#fff"/></svg>Thatch Removal</li>
    <li><svg width="18" height="18" viewBox="0 0 18 18"><circle cx="9" cy="9" r="8" fill="#4cc23a"/><circle cx="9" cy="9" r="4" fill="#fff"/></svg><span>Fertilizer &amp; Weed Control Applications<br>(Programs Available)</span></li>
    <li><svg width="18" height="18" viewBox="0 0 18 18"><circle cx="9" cy="9" r="8" fill="#4cc23a"/><circle cx="9" cy="9" r="4" fill="#fff"/></svg>Spring &amp; Fall Clean ups</li>
  </ul>
  <ul class="services services-right">
    <li><svg width="18" height="18" viewBox="0 0 18 18"><circle cx="9" cy="9" r="8" fill="#4cc23a"/><circle cx="9" cy="9" r="4" fill="#fff"/></svg>New Lawn Installations</li>
    <li><svg width="18" height="18" viewBox="0 0 18 18"><circle cx="9" cy="9" r="8" fill="#4cc23a"/><circle cx="9" cy="9" r="4" fill="#fff"/></svg>Pruning</li>
    <li><svg width="18" height="18" viewBox="0 0 18 18"><circle cx="9" cy="9" r="8" fill="#4cc23a"/><circle cx="9" cy="9" r="4" fill="#fff"/></svg>Mulch and rock Installation</li>
    <li><svg width="18" height="18" viewBox="0 0 18 18"><circle cx="9" cy="9" r="8" fill="#4cc23a"/><circle cx="9" cy="9" r="4" fill="#fff"/></svg>Hedge Trimming</li>
    <li><svg width="18" height="18" viewBox="0 0 18 18"><circle cx="9" cy="9" r="8" fill="#4cc23a"/><circle cx="9" cy="9" r="4" fill="#fff"/></svg><span>Winter Snow Removal Services<br>&amp; more</span></li>
  </ul>

  <section class="special-offer">
    <p class="offer-title">Let us earn your Business</p>
    <p class="offer-terms">Call now and get your first cut free of charge. *conditions apply</p>
  </section>

  <div class="divider"></div>
  <p class="free-estimates"><span class="big">Free</span> Estimates</p>
  <p class="fully-insured"><span class="big">Fully</span> Insured</p>

  <div class="contact-bar">
    <div class="phone">PHONE: 506-384-9057</div>
    <div class="email">EMAIL:<br>ADMIN@BRIARTOPLANDSCAPING.CA</div>
  </div>

  <p class="service-area">Serving Saint John &amp; Surrounding Areas</p>
</main>
</body>
</html>
```